Poster Design Project - Quill Bar and Restaurant

We require a Horse Racing Carnival poster (Tarrawong Autumn Turf Festival) to showcase the offer at our Bar/Restaurant.

The venue is called QUILL. Our website is www.quillbar-example.com.au

The venue is heavily design focused with significant use of strong graphics and logos.

The poster will need to be printed out in AO size.
Updates

Once again, thank you all for participating in this design creation. We are going to list a number of other poster briefs shortly that will require strong quirky/design graphics. I hope you'll all participate.

I am happy to provide individual responses to queries about specific designs and why they have been unsuccessful.

Overall we were really impressed with the quality of the submissions.

Thanks Gavin

Target Market(s)

Our demographic is 25-35 years old

Industry/Entity Type

Restaurant

Requirements
Must have
• The following copy needs to be incorporated into the poster -

QUILL

AUTUMN TURF FESTIVAL 2011

Lantern Day - 29th October 2011
Champagne breakfast from 9am
Buses to and from the track
$15 bus ticket includes redeemable drink voucher
DJ from 8pm until 3am

Tarrawong Plate Eve - 31st October 2011
Drink specials all night
DJ from 8pm until close

Tarrawong Plate Day - 1st November 2011
Big screen racing live on 3 screens
Cocktail and drinks specials all day
DJ from 4pm

Fillies Gala - 3rd November 2011
DJ from 8pm until close

Closing Run - 5th November 2011
The finishing post - Complimentary glass of sparkling with presentation of race entry ticket
DJ's from 9pm until 3am

For further enquiries and to secure your bus tickets please contact Corinne on 84172059.

178 Wexford Lane, Port Delvin Vic 3902
Tel: 84172059
Twitter: @thequillbar
Facebook: Quill Bar and Restaurant
www.quillbar-example.com.au
Should not have
• No cheesy graphics

```html
<!DOCTYPE html>
<html lang="en">
<head>
<meta charset="utf-8">
<title>Quill – Autumn Turf Festival 2011</title>
<link rel="stylesheet" href="https://fonts.googleapis.com/css2?family=Fredoka:wght@600&family=Ubuntu:wght@400;500;700&display=swap">
<style>
  :root {
    --paper: #d3b597;
    --ink: #111111;
    --band: #000000;
    --sun: #fff200;
    --red: #e8202a;
    --green: #3fae49;
    --blue: #1f8fd6;
    --orange: #f39200;
    --leaf: #2fa836;
    --card: #d89c55;
    --card-edge: #c2823d;
    --tape: rgba(250, 240, 185, 0.72);
    --horse: #151515;
  }
  html, body {
    margin: 0;
    padding: 0;
    overflow: hidden;
  }
  .poster {
    position: relative;
    width: 850px;
    height: 1200px;
    background: var(--paper);
    overflow: hidden;
    font-family: "Ubuntu", sans-serif;
    color: var(--ink);
  }
  .venue-name {
    position: absolute;
    top: 14px;
    left: 0;
    width: 850px;
    margin: 0;
    text-align: center;
    font-family: "Fredoka", sans-serif;
    font-weight: 600;
    font-size: 196px;
    line-height: 200px;
    letter-spacing: 34px;
    text-indent: 34px;
    color: var(--sun);
  }
  .festival-band {
    position: absolute;
    top: 214px;
    left: 0;
    width: 850px;
    height: 50px;
    background: var(--band);
    display: flex;
    align-items: center;
    justify-content: center;
  }
  .festival-title {
    margin: 0;
    font-family: "Fredoka", sans-serif;
    font-weight: 600;
    font-size: 44px;
    letter-spacing: 2px;
    color: var(--sun);
    white-space: nowrap;
  }
  .festival-title .c-red { color: var(--red); }
  .festival-title .c-green { color: var(--green); }
  .festival-title .c-blue { color: var(--blue); }
  .festival-title .c-yellow { color: var(--sun); }
  .festival-title .c-orange { color: var(--orange); }

  .event-card {
    position: absolute;
    box-sizing: border-box;
    background:
      repeating-linear-gradient(90deg, rgba(0,0,0,0.035) 0 2px, transparent 2px 6px),
      var(--card);
    border: 1px solid var(--card-edge);
    box-shadow: 0 2px 4px rgba(0,0,0,0.18);
    padding: 26px 20px 16px 58px;
  }
  .event-card h2 {
    margin: 0;
    color: var(--leaf);
    font-weight: 700;
    font-size: 22px;
    line-height: 28px;
  }
  .event-card ul {
    list-style: none;
    margin: 2px 0 0;
    padding: 0;
    font-size: 17px;
    line-height: 22px;
  }
  .card-lantern   { left: 46px;  top: 350px; width: 348px; height: 214px; transform: rotate(-4deg); padding-left: 66px; padding-top: 34px; }
  .card-plate-day { left: 428px; top: 308px; width: 362px; height: 192px; transform: rotate(2deg); padding-left: 48px; padding-top: 18px; }
  .card-fillies   { left: 458px; top: 552px; width: 342px; height: 198px; transform: rotate(2deg); padding-left: 48px; padding-top: 18px; }
  .card-plate-eve { left: 56px;  top: 704px; width: 284px; height: 124px; transform: rotate(-4deg); padding-left: 48px; padding-top: 16px; }
  .card-plate-eve h2 { font-size: 20px; line-height: 24px; }
  .card-closing   { left: 374px; top: 784px; width: 426px; height: 214px; transform: rotate(3deg); padding-left: 42px; padding-top: 22px; }
  .card-closing .indent { padding-left: 30px; }

  .tape {
    position: absolute;
    width: 100px;
    height: 34px;
    background: var(--tape);
    box-shadow: 0 1px 2px rgba(0,0,0,0.08);
  }
  .tape-1 { left: 14px;  top: 352px; width: 118px; transform: rotate(-24deg); }
  .tape-2 { left: 330px; top: 540px; transform: rotate(-38deg); }
  .tape-3 { left: 690px; top: 316px; transform: rotate(32deg); }
  .tape-4 { left: 370px; top: 472px; transform: rotate(42deg); }
  .tape-5 { left: 404px; top: 568px; transform: rotate(-34deg); }
  .tape-6 { left: 730px; top: 724px; transform: rotate(28deg); }
  .tape-7 { left: 20px;  top: 818px; transform: rotate(36deg); }
  .tape-8 { left: 700px; top: 784px; transform: rotate(40deg); }
  .tape-9 { left: 330px; top: 952px; transform: rotate(32deg); }

  .horse-art {
    position: absolute;
    left: 0;
    top: 846px;
    width: 326px;
    height: 354px;
    background: linear-gradient(160deg, var(--horse) 0%, #2a2a2a 100%);
    border-top-right-radius: 160px 120px;
  }

  .contact {
    position: absolute;
    left: 330px;
    top: 1040px;
    width: 480px;
    text-align: center;
  }
  .contact-lead {
    margin: 0 0 12px;
    font-weight: 700;
    font-size: 17px;
    line-height: 21px;
  }
  .contact-lead strong { font-size: 22px; }
  .contact-details {
    margin: 0;
    font-weight: 700;
    font-size: 14px;
    line-height: 20px;
  }
</style>
</head>
<body>
<main class="poster">
  <h1 class="venue-name">QUILL</h1>

  <div class="festival-band">
    <p class="festival-title"><span class="c-red">A</span><span class="c-green">U</span><span class="c-blue">T</span><span class="c-yellow">U</span><span class="c-orange">M</span><span class="c-green">N</span> TURF FESTIVAL 2011</p>
  </div>

  <section class="event-card card-plate-day">
    <h2>Tarrawong Plate Day<br>1st November 2011</h2>
    <ul>
      <li>Champagne breakfast from 9am</li>
      <li>Big screen racing live on 3 screens</li>
      <li>Cocktail and drinks specials all day</li>
      <li>DJ from 4pm</li>
    </ul>
  </section>

  <section class="event-card card-lantern">
    <h2>Lantern Day<br>29th October 2011</h2>
    <ul>
      <li>Champagne breakfast from 9am</li>
      <li>Buses to and from the track</li>
      <li>$15 bus ticket includes</li>
      <li>redeemable drink voucher</li>
      <li>DJ from 8pm until 3am</li>
    </ul>
  </section>

  <section class="event-card card-fillies">
    <h2>Fillies Gala<br>3rd November 2011</h2>
    <ul>
      <li>Champagne breakfast from 9am</li>
      <li>Buses to and from the track</li>
      <li>$15 bus ticket includes</li>
      <li>redeemable drink voucher</li>
      <li>DJ from 8pm until close</li>
    </ul>
  </section>

  <section class="event-card card-plate-eve">
    <h2>Tarrawong Plate Eve<br>31st October 2011</h2>
    <ul>
      <li>Drink specials all night</li>
      <li>DJ from 8pm until close</li>
    </ul>
  </section>

  <section class="event-card card-closing">
    <h2>Closing Run<br>5th November 2011</h2>
    <ul>
      <li>The finishing post</li>
      <li>Complimentary glass of sparkling</li>
      <li>with presentation of race entry ticket</li>
      <li class="indent">DJ's from 9pm until 3am</li>
    </ul>
  </section>

  <div class="tape tape-1"></div>
  <div class="tape tape-2"></div>
  <div class="tape tape-3"></div>
  <div class="tape tape-4"></div>
  <div class="tape tape-5"></div>
  <div class="tape tape-6"></div>
  <div class="tape tape-7"></div>
  <div class="tape tape-8"></div>
  <div class="tape tape-9"></div>

  <div class="horse-art" role="img" aria-label="Black silhouette of a jockey riding a galloping racehorse"></div>

  <footer class="contact">
    <p class="contact-lead">For further enquiries and to secure your bus tickets<br>please <strong>contact Corinne</strong> on <strong>84172059.</strong></p>
    <p class="contact-details">
      178 Wexford Lane, Port Delvin Vic 3902 &nbsp;|&nbsp; Tel: 84172059<br>
      Twitter: @thequillbar<br>
      Facebook: Quill Bar and Restaurant<br>
      www.quillbar-example.com.au
    </p>
  </footer>
</main>
</body>
</html>
```